Brightmoor Learning Brochure Design Project

Our company requires a brochure for promoting our Corporate Training business.

Please use data from Corporate training brochure doc.
Updates

Dear Designers,

We have added new corporate brochure document into the project. Use this data to finish up your brochure.

Thanks,

Omar Kasprzak

Reason: We have recently finalised the data that will go into the corporate brochure.

Reason: To get more better designs

Target Market(s)

Training Managers / Business Managers / Hiring Managers

Industry/Entity Type

Training

Requirements
Must have
• Corporate and Professional Look

```html
<!DOCTYPE html>
<html lang="en">
<head>
<meta charset="utf-8">
<title>Brightmoor Learning – Corporate Customised IT Training</title>
<link rel="stylesheet" href="https://fonts.googleapis.com/css2?family=Saira+Condensed:wght@300;400&display=swap">
<style>
  :root {
    --sky: #3fa9e0;
    --sky-light: #8fd0f2;
    --sky-pale: #cfeafa;
    --navy: #0f3d66;
    --ink: #3a3a3a;
    --rule: #c9c9c9;
    --band: #0d5a7e;
    --paper: #ffffff;
    --photo-top: #6f7466;
    --photo-mid: #8d9a7a;
    --photo-low: #4d5548;
    --tint-a: #2b7fb8;
    --tint-b: #7ec3e6;
  }
  * { margin: 0; padding: 0; box-sizing: border-box; }
  html, body { width: 1200px; height: 2770px; overflow: hidden; background: var(--paper); }
  .brochure {
    position: relative;
    width: 1200px;
    height: 2770px;
    overflow: hidden;
    background: var(--paper);
    font-family: "Saira Condensed", "Arial Narrow", sans-serif;
    font-weight: 300;
  }
  .hero { position: absolute; inset: 0 0 auto 0; width: 1200px; height: 1560px; }
  .brand {
    position: absolute; top: 1370px; left: 0; width: 1200px;
    text-align: center; color: var(--sky);
    font-size: 150px; line-height: 1; letter-spacing: 1px;
  }
  .tagline {
    position: absolute; top: 1595px; left: 0; width: 1200px;
    text-align: center; color: var(--ink); font-size: 64px; line-height: 1;
  }
  .rule {
    position: absolute; left: 0; width: 1200px; height: 3px; background: var(--rule);
  }
  .rule--short { left: 133px; width: 934px; top: 1705px; }
  .rule--short::after {
    content: ""; position: absolute; left: 10%; right: 10%; top: 3px; height: 60px;
    background: radial-gradient(ellipse at top, rgba(0,0,0,0.08), rgba(0,0,0,0) 70%);
  }
  .rule--a { top: 2085px; }
  .rule--b { top: 2265px; }
  .rule--c { top: 2432px; }
  .pitch { position: absolute; top: 1880px; left: 133px; width: 940px; color: var(--ink); line-height: 1; }
  .pitch__lead { display: block; font-size: 58px; }
  .pitch__close { display: block; text-align: right; font-size: 72px; margin-top: 6px; }
  .promise {
    position: absolute; top: 2118px; left: 0; width: 1200px; text-align: center;
    color: var(--sky); font-size: 72px; line-height: 1; font-weight: 400;
  }
  .question {
    position: absolute; top: 2305px; left: 0; width: 1200px; text-align: center;
    color: var(--navy); font-size: 62px; line-height: 1; font-weight: 400;
  }
  .footer-band { position: absolute; left: 0; bottom: 0; width: 1200px; height: 44px; background: var(--band); }
</style>
</head>
<body>
<main class="brochure">
  <svg class="hero" viewBox="0 0 1200 1560" xmlns="http://www.w3.org/2000/svg">
    <defs>
      <linearGradient id="photoTone" x1="0" y1="0" x2="0" y2="1">
        <stop offset="0" stop-color="var(--photo-top)"/>
        <stop offset="0.45" stop-color="var(--photo-mid)"/>
        <stop offset="1" stop-color="var(--photo-low)"/>
      </linearGradient>
      <linearGradient id="tintTone" x1="0" y1="0" x2="1" y2="1">
        <stop offset="0" stop-color="var(--tint-a)"/>
        <stop offset="1" stop-color="var(--tint-b)"/>
      </linearGradient>
    </defs>
    <rect class="hero__photo" x="0" y="0" width="1200" height="1560" fill="url(#photoTone)"
          role="img" aria-label="Photo of a businesswoman in a beige blazer seated beside planters of tall green plants in an office courtyard"/>
    <path class="hero__tint" d="M1200,200 C 800,300 420,620 300,1000 C 560,860 900,1000 1200,1520 Z"
          fill="url(#tintTone)" role="img" aria-label="Blue-tinted view of the courtyard planters"/>
    <path class="hero__arc hero__arc--outer" d="M0,1300 C 250,760 700,330 1200,180" fill="none" stroke="var(--sky-pale)" stroke-width="60"/>
    <path class="hero__arc hero__arc--main" d="M0,1320 C 260,790 720,360 1200,225" fill="none" stroke="var(--sky)" stroke-width="34"/>
    <path class="hero__arc hero__arc--inner" d="M20,1350 C 290,830 740,420 1200,290" fill="none" stroke="var(--sky-light)" stroke-width="22"/>
    <path class="hero__paper" d="M0,1290 C 260,1000 500,820 740,820 C 960,820 1120,1120 1200,1540 L1200,1560 L0,1560 Z" fill="var(--paper)"/>
    <path class="hero__edge" d="M0,1290 C 260,1000 500,820 740,820 C 960,820 1120,1120 1200,1540" fill="none" stroke="var(--sky-pale)" stroke-width="16"/>
  </svg>

  <h1 class="brand">Brightmoor Learning</h1>
  <p class="tagline">Corporate Customised IT Training</p>
  <div class="rule rule--short"></div>

  <p class="pitch">
    <span class="pitch__lead">Get a Training Program as exclusive as</span>
    <span class="pitch__close">your business needs</span>
  </p>
  <div class="rule rule--a"></div>
  <p class="promise">Love our training or your money back!</p>
  <div class="rule rule--b"></div>
  <p class="question">If you could improve your business would you?</p>
  <div class="rule rule--c"></div>

  <div class="footer-band"></div>
</main>
</body>
</html>
```